Brovani Brochure

Investment company brochure related to FOREX

Industry/Entity Type

Investment

Requirements
Must have
• www.brovanigroup.com
• www.kwhmarkets.com

```html
<!DOCTYPE html>
<html lang="en">
<head>
<meta charset="utf-8">
<title>Brovani Brochure</title>
<link rel="stylesheet" href="https://fonts.googleapis.com/css2?family=Arimo:ital,wght@0,400;0,700;1,400&family=Jura:wght@400;500&family=Michroma&display=swap">
<style>
  :root {
    --stage: #000000;
    --red: #c8101c;
    --red-deep: #8e0a12;
    --red-bright: #e3202c;
    --red-soft: #f05a62;
    --white: #ffffff;
    --paper-grey: #f1eeee;
    --text-grey: #6b6b6b;
    --strip-grey: #5d5d5d;
    --accent-orange: #f08a1c;
    --photo-tone-a: #c9ccd2;
    --photo-tone-b: #8f949c;
  }
  * { box-sizing: border-box; margin: 0; padding: 0; }
  html, body { width: 1200px; height: 853px; overflow: hidden; background: var(--stage); }
  .canvas { position: relative; width: 1200px; height: 853px; background: var(--stage); overflow: hidden; font-family: "Arimo", Arial, sans-serif; }

  .panel { position: absolute; top: 170px; width: 360px; height: 510px; background: var(--white); overflow: hidden; }
  .panel--about { left: 40px; }
  .panel--services { left: 400px; background: linear-gradient(180deg, var(--white) 0%, var(--paper-grey) 55%, var(--white) 100%); }
  .panel--cover { left: 800px; }

  /* About Us */
  .about__band {
    position: absolute; left: 0; top: 0; width: 360px; height: 240px;
    background: radial-gradient(ellipse at 70% 30%, var(--red-bright) 0%, var(--red) 45%, var(--red-deep) 100%);
    clip-path: polygon(0 0, 100% 0, 100% 225px, 340px 225px, 330px 238px, 320px 225px, 0 225px);
  }
  .about__title { position: absolute; right: 22px; top: 70px; font-family: "Jura", sans-serif; font-size: 24px; color: var(--white); }
  .about__rule { position: absolute; left: 0; right: 22px; top: 104px; height: 1px; background: rgba(255,255,255,.7); }
  .about__heading { position: absolute; right: 22px; left: 30px; top: 128px; text-align: right; font-style: italic; font-size: 16px; line-height: 21px; color: var(--white); }
  .about__heading em { color: var(--red-soft); }
  .about__body { position: absolute; left: 18px; right: 22px; top: 252px; font-size: 8.5px; line-height: 12px; color: var(--text-grey); }
  .about__lead { position: absolute; left: 18px; top: 370px; font-style: italic; font-size: 10px; color: var(--red); }
  .about__list { position: absolute; left: 18px; top: 390px; list-style: none; font-style: italic; font-size: 9.5px; line-height: 15px; color: var(--red); }
  .about__list li::before { content: "›"; font-weight: 700; margin-right: 6px; }
  .about__footer { position: absolute; left: 0; bottom: 0; width: 100%; height: 24px; background: linear-gradient(90deg, var(--red-deep), var(--red)); color: var(--white); font-size: 8.5px; letter-spacing: .5px; padding: 8px 18px; text-transform: uppercase; }

  /* Services */
  .services__band { position: absolute; left: 0; top: 0; width: 360px; height: 60px; background: linear-gradient(90deg, var(--red-deep), var(--red) 60%, var(--red-bright)); }
  .services__title { position: absolute; right: 14px; top: 14px; font-family: "Jura", sans-serif; font-size: 22px; color: var(--white); }
  .services__rule { position: absolute; left: 120px; right: 14px; top: 46px; }
  .service { position: absolute; left: 14px; right: 16px; }
  .service__title { font-size: 12.5px; color: var(--red-bright); margin-bottom: 5px; }
  .service__text { font-size: 8.3px; line-height: 11.2px; color: var(--text-grey); }
  .service--fx { top: 78px; }
  .service--risk { top: 148px; }
  .service--credit { top: 272px; }
  .services__footer { position: absolute; left: 0; bottom: 0; width: 100%; height: 28px; background: linear-gradient(90deg, var(--red-deep), var(--red)); color: var(--white); font-size: 8.5px; letter-spacing: .6px; text-align: right; padding: 10px 14px; text-transform: uppercase; }

  /* Cover */
  .cover__band { position: absolute; left: 0; top: 0; width: 360px; height: 300px; background: linear-gradient(90deg, var(--red-deep) 0%, var(--red) 55%, var(--red-bright) 100%); }
  .cover__accent { position: absolute; left: 0; top: 300px; width: 360px; height: 3px; background: var(--accent-orange); }
  .cover__list { position: absolute; right: 24px; top: 138px; list-style: none; text-align: right; }
  .cover__list li { position: relative; font-family: "Michroma", sans-serif; font-size: 9.5px; letter-spacing: 1px; color: var(--white); height: 35px; padding-right: 14px; }
  .cover__list li::after { content: ""; position: absolute; right: -4px; top: 2px; width: 7px; height: 7px; border-radius: 50%; background: var(--white); }
  .cover__line { position: absolute; right: 27px; top: 143px; width: 1px; height: 105px; background: rgba(255,255,255,.8); }
  .cover__photo { position: absolute; left: 0; top: 330px; width: 230px; height: 152px; background: linear-gradient(180deg, var(--photo-tone-a), var(--photo-tone-b)); }
  .cover__logo { position: absolute; right: 26px; top: 388px; font-family: "Michroma", sans-serif; font-size: 9px; letter-spacing: 1px; color: var(--red); }
  .cover__strip { position: absolute; left: 0; bottom: 0; width: 360px; height: 28px; background: var(--strip-grey); }
</style>
</head>
<body>
<main class="canvas">

  <section class="panel panel--about">
    <div class="about__band"></div>
    <h2 class="about__title">About Us</h2>
    <div class="about__rule"></div>
    <p class="about__heading"><em>Heading Text</em> here Heading Text here Heading Text here Heading Text hereHeading Text</p>
    <p class="about__body">Subtext here Subtext here Subtext here Subtext here Subtext here Subtext here Subtext here Subtext here Subtext here Subtext here Subtext here Subtext here Subtext here Subtext here Subtext here Subtext here Subtext here Subtext here Subtext here Subtext here Subtext here Subtext here Subtext here Subtext here Subtext here Subtext here Subtext here Subtext here Subtext here Subtext here Subtext here Subtext here Subtext here Subtext here Subtext here Subtext here Subtext here Subtext here Subtext here Subtext here Subtext here Subtext here</p>
    <p class="about__lead">The services our partners provide are :</p>
    <ul class="about__list">
      <li>Foreign exchange service</li>
      <li>Covering financial risks</li>
      <li>Trade credit insurance</li>
      <li>Bonding</li>
      <li>Trade debt collections</li>
      <li>Factoring</li>
    </ul>
    <footer class="about__footer">www.brovanigroup.com</footer>
  </section>

  <section class="panel panel--services">
    <div class="services__band"></div>
    <h2 class="services__title">Our Services</h2>
    <svg class="services__rule" width="226" height="10" viewBox="0 0 226 10" aria-hidden="true">
      <polyline points="0,1 210,1 216,8 222,1 226,1" fill="none" stroke="#ffffff" stroke-width="1"/>
    </svg>
    <article class="service service--fx">
      <h3 class="service__title">Foreign Exchange Service</h3>
      <p class="service__text">Subtext here Subtext here Subtext here Subtext here Subtext here Subtext here Subtext here Subtext here Subtext here Subtext here Subtext here Subtext here Subtext here Subtext here Subtext here Subtext here Subtext here Subtext here</p>
    </article>
    <article class="service service--risk">
      <h3 class="service__title">Covering Financial Risks</h3>
      <p class="service__text">Subtext here Subtext here Subtext here Subtext here Subtext here Subtext here Subtext here Subtext here Subtext here Subtext here Subtext here Subtext here Subtext here Subtext here Subtext here Subtext here Subtext here Subtext here Subtext here Subtext here Subtext here Subtext here Subtext here Subtext here Subtext here Subtext here Subtext here Subtext here Subtext here Subtext here Subtext here Subtext here Subtext here Subtext here Subtext here Subtext here Subtext here Subtext here Subtext here Subtext here Subtext here Subtext here Subtext here Subtext here Subtext here Subtext here Subtext here</p>
    </article>
    <article class="service service--credit">
      <h3 class="service__title">Trade Credit Insurance</h3>
      <p class="service__text">Subtext here Subtext here Subtext here Subtext here Subtext here Subtext here Subtext here Subtext here Subtext here Subtext here Subtext here Subtext here Subtext here Subtext here Subtext here Subtext here Subtext here Subtext here Subtext here Subtext here Subtext here Subtext here Subtext here Subtext here Subtext here Subtext here Subtext here Subtext here Subtext here Subtext here Subtext here Subtext here Subtext here Subtext here Subtext here Subtext here Subtext here Subtext here Subtext here Subtext here Subtext here Subtext here Subtext here Subtext here Subtext here Subtext here Subtext here Subtext here Subtext here Subtext here Subtext here Subtext here Subtext here Subtext here Subtext here Subtext here Subtext here Subtext here</p>
    </article>
    <footer class="services__footer">www.kwhmarkets.com</footer>
  </section>

  <section class="panel panel--cover">
    <div class="cover__band"></div>
    <div class="cover__line"></div>
    <ul class="cover__list">
      <li>BUSINESS VALUATIONS</li>
      <li>BUSINESS TURNAROUND</li>
      <li>DUE DILIGENCE</li>
      <li>BUSINESS STRUCTURING</li>
    </ul>
    <div class="cover__accent"></div>
    <div class="cover__photo" role="img" aria-label="Photo of a team of four business professionals in suits"></div>
    <p class="cover__logo">LOGO TEXT</p>
    <div class="cover__strip"></div>
  </section>

</main>
</body>
</html>
```